Erstellung Etikettendesign für Duschgel in Motorölflaschenoptik als Geschenkartikel für Männer
Zielgruppe
Wir sind Versandhändler aus dem Bereich Büro Basteln Schule und Geschenkartikel und verkaufen neben Handelsware aus diesem Bereich auch viele eigene selbst gestaltete Artikel unter unserem Firmennamen morvalo
Aufgabenstellung
Erstellt werden soll ein neues zusätzliches Etikettendesign für unseren Artikel Duschgel für Männer
Das Duschgel wird in Form in einer Motorölflasche geliefert und ist so ein Geschenkartikel für Männer zum Geburtstag, Weihnachten, Vatertag usw.
Die Flaschenfarbe ist immer schwarz
und der Verschluss ist rot
bzgl dem Etikettendesign sind wir für alle kreativen Ideen offen.
Es dürfen allerdings keine anderen Markenrechte verletzt werden
Unter dem Link
https://www.kaufwelt-shop.de/dp/K7R2MXQ9D3
finden sie unsere aktuellen Designs.
Bei solchen Designumsetzungen ist natürlich immer darauf zu achten nicht zu nahe an einem geschützten Produktdesign zu liegen.
Es werden hier mehrere Ideen gesammelt
Es wird bei guten Entwürfen auch mehrere Gewinner geben und mehrere Designs kommen zur Umsetzung.
Nach Auswahl zum Gewinner müssten dann noch die Druckdatei für die Etiketten und ein Produktfoto erstellt werden.
Vorlage für Druckdatei und Beispiel Produktfoto anbei
Aufgabe ist hierbei nicht das Design KL-73 anders umzusetzen sondern andere ganz neue Ideen als Etikett umzusetzen

```html
<!DOCTYPE html>
<html lang="de">
<head>
<meta charset="UTF-8">
<title>Recken Tank – Duschgel Etikett</title>
<link rel="stylesheet" href="https://fonts.googleapis.com/css2?family=Montserrat:wght@800;900&family=Barlow+Semi+Condensed:wght@600;700&family=Barlow:wght@600;700&display=swap">
<style>
  :root {
    --bg: #cfcfcf;
    --label-black: #0c0c0c;
    --lime: #7cc41a;
    --gauge-green: #35c03c;
    --gauge-dark: #12331a;
    --power-green: #3dbb3a;
    --white: #ececec;
  }
  * { margin: 0; padding: 0; box-sizing: border-box; }
  html, body {
    width: 800px;
    height: 1200px;
    overflow: hidden;
    background: var(--bg);
  }
  .canvas {
    position: relative;
    width: 800px;
    height: 1200px;
    display: flex;
    align-items: center;
    justify-content: center;
  }
  .label {
    position: relative;
    width: 620px;
    height: 1120px;
    background: var(--label-black);
    clip-path: polygon(250px 0, 100% 0, 100% 100%, 0 100%, 0 130px);
    border-radius: 0 18px 18px 18px;
    display: flex;
    flex-direction: column;
    align-items: center;
    padding-top: 165px;
    text-align: center;
  }
  .brand-title {
    font-family: "Montserrat", sans-serif;
    font-weight: 900;
    color: var(--lime);
    line-height: 0.92;
    letter-spacing: -2px;
  }
  .brand-title .line-top { display: block; font-size: 112px; }
  .brand-title .line-bottom { display: block; font-size: 178px; letter-spacing: -4px; }
  .claim {
    margin-top: 30px;
    font-family: "Barlow", sans-serif;
    font-weight: 700;
    color: var(--white);
    line-height: 1.05;
  }
  .claim .claim-small { display: block; font-size: 42px; letter-spacing: 1px; }
  .claim .claim-large { display: block; font-size: 58px; letter-spacing: 2px; }
  .gauge-art {
    margin-top: 30px;
    width: 480px;
    height: 240px;
    border-radius: 240px 240px 0 0;
    background: radial-gradient(circle at 50% 100%, var(--gauge-dark) 0%, var(--gauge-dark) 55%, var(--gauge-green) 100%);
  }
  .slogan {
    margin-top: 44px;
    font-family: "Barlow Semi Condensed", sans-serif;
    font-weight: 700;
    font-size: 50px;
    color: var(--white);
  }
  .variant {
    margin-top: 10px;
    font-family: "Barlow", sans-serif;
    font-weight: 700;
    font-size: 48px;
    color: var(--power-green);
  }
  .product-type {
    margin-top: 12px;
    font-family: "Barlow", sans-serif;
    font-weight: 600;
    font-size: 38px;
    letter-spacing: 1.5px;
    color: var(--white);
  }
</style>
</head>
<body>
<main class="canvas">
  <section class="label">
    <h1 class="brand-title">
      <span class="line-top">RECKEN</span>
      <span class="line-bottom">TANK</span>
    </h1>
    <p class="claim">
      <span class="claim-small">100% KONZENTRIERTE</span>
      <span class="claim-large">MÄNNLICHKEIT</span>
    </p>
    <div class="gauge-art" role="img" aria-label="Tachometer-Illustration mit grüner Skala, Bizeps-Symbol und roter Nadel im oberen Bereich"></div>
    <p class="slogan">EIN SCHWAPP REICHT!</p>
    <p class="variant">MENTHOL POWER</p>
    <p class="product-type">DUSCHGEL FÜR MÄNNER</p>
  </section>
</main>
</body>
</html>
```